Order Form Template

We are looking to develop a professional looking order form, also see attached a brochure of our solution to see how nice it is from the brochure, I also attached devices logos. I would like to have the devices nd plans in multiple lines and quantity and price and total price. also leave a space below for a policy of billing and cancellation which we will add ourself later.

```html
<!DOCTYPE html>
<html lang="en">
<head>
<meta charset="utf-8">
<title>Northgate Tracking – Order Form Set</title>
<link rel="stylesheet" href="https://fonts.googleapis.com/css2?family=Montserrat:wght@400;500;600;700&display=swap">
<style>
:root{
  --brand:#3589bb;
  --brand-text:#3a84b6;
  --tint:#b9dff0;
  --rule:#4e96c4;
  --paper:#ffffff;
  --ground:#e6e8ea;
  --photo-dark:#2b2f38;
  --photo-mid:#5b6472;
}
*{box-sizing:border-box;margin:0;padding:0}
html,body{width:1015px;height:1200px;overflow:hidden}
body{background:var(--ground);font-family:"Montserrat",sans-serif;position:relative;color:var(--brand-text)}

.page{position:absolute;width:339px;height:438px;background:var(--paper);box-shadow:0 2px 6px rgba(0,0,0,.12)}
.page--order{left:131px;top:121px}
.page--plans{left:529px;top:121px}
.page--terms{left:322px;top:610px}

.masthead{position:absolute;left:0;top:0;width:100%;height:53px}
.masthead__panel{position:absolute;inset:0}
.brand{position:absolute;left:18px;top:18px;display:flex;align-items:center;gap:5px}
.brand__mark{width:17px;height:17px;border-radius:50%;background:var(--brand)}
.brand__name{font-size:12.5px;font-weight:600;color:var(--brand);letter-spacing:.2px}
.company{position:absolute;right:19px;top:10px;text-align:right;color:#fff;font-style:normal;font-size:6.2px;line-height:8.6px}
.company strong{font-weight:700;font-size:6.6px}

.title-band{position:absolute;left:0;top:53px;width:100%;height:20px;background:var(--brand);
  color:#fff;font-weight:700;font-size:7.6px;text-align:center;line-height:20px;letter-spacing:.2px}
.footer-band{position:absolute;left:0;bottom:0;width:100%;height:16px;background:var(--brand);
  color:#fff;font-weight:700;font-size:5.6px;text-align:center;line-height:16px}

.block{position:absolute;left:20px;width:299px;border:1px solid var(--rule)}
.block__head{background:var(--brand);color:#fff;font-weight:600;font-size:6.6px;text-align:center;height:11px;line-height:11px}
.row{display:flex;border-top:1px solid var(--rule)}
.cell{flex:1;font-size:5.2px;font-weight:600;padding:0 3px;border-left:1px solid var(--rule);line-height:9px}
.cell:first-child{border-left:none}
.row--label .cell{background:var(--tint);text-align:center}
.row--blank{height:10px}
.row--blank .cell{height:9px}
.cell--left{text-align:left!important;padding-left:9px}

.method .cell{height:19px;text-align:center}
.method .cell:first-child{flex:3;text-align:left;padding-left:4px}

.card-rows .row{height:10.7px}
.card-rows .cell{line-height:9.7px;text-align:left}

.product{display:flex;height:49px;border-top:1px solid var(--rule)}
.product:first-child{border-top:none}
.product__photo{width:100px;border-right:1px solid var(--rule);display:flex;align-items:center;justify-content:center}
.product__photo span{display:block;width:64px;height:36px;border-radius:5px;
  background:linear-gradient(135deg,var(--photo-mid),var(--photo-dark))}
.product__body{flex:1;display:flex;flex-direction:column}
.product__details{flex:1;font-size:5.2px;font-weight:600;padding:3px 3px}
.product__figures{display:flex;height:16px;background:var(--tint);border-top:1px solid var(--rule)}
.product__figures div{flex:1;font-size:5.2px;font-weight:600;padding:3px;border-left:1px solid var(--rule)}
.product__figures div:first-child{border-left:none}

.plans{display:flex;height:60px;border-top:1px solid var(--rule)}
.plans__spacer{width:100px;border-right:1px solid var(--rule)}
.plans__list{flex:1;padding:6px 3px;font-size:6.1px;font-weight:600;line-height:10.6px}
.box{display:inline-block;width:5.5px;height:5.5px;border:.7px solid var(--brand-text);margin-right:2px;vertical-align:-.5px;position:relative}
.box--checked::before,.box--checked::after{content:"";position:absolute;left:50%;top:-1px;width:.7px;height:6.5px;background:var(--brand-text)}
.box--checked::before{transform:rotate(45deg)}
.box--checked::after{transform:rotate(-45deg)}
.sign{height:25px;background:var(--tint);border-top:1px solid var(--rule);font-size:5.2px;font-weight:600;padding:3px}
.signoff{display:flex;height:24px;border-top:1px solid var(--rule)}
.signoff div{font-size:5.2px;font-weight:600;padding:3px}
.signoff div:first-child{width:149px;border-right:1px solid var(--rule)}
.note{height:62px;background:var(--tint);border-top:1px solid var(--rule);font-size:5.2px;font-weight:600;padding:3px}
</style>
</head>
<body>

<section class="page page--order">
  <header class="masthead">
    <svg class="masthead__panel" viewBox="0 0 339 53" preserveAspectRatio="none" aria-hidden="true"><polygon points="232,0 339,0 339,53 208,53" fill="#3589bb"/></svg>
    <div class="brand"><span class="brand__mark"></span><span class="brand__name">NORTHGATE</span></div>
    <address class="company"><strong>Northgate Tracking Ltd.</strong><br>418 Rue Marlowe, Quebec<br>H2X 4B7 Canada<br>1800 555 0142</address>
  </header>
  <h1 class="title-band">PAYMENT AUTHORIZATION</h1>

  <div class="block" style="top:85px">
    <div class="block__head">Customer Contact Information</div>
    <div class="row row--label"><div class="cell">Customer Company Name</div><div class="cell">Billing Contact Name</div><div class="cell">Billing E-Mail Address</div></div>
    <div class="row row--blank"><div class="cell"></div></div>
    <div class="row row--label"><div class="cell cell--left" style="flex:2">Billing Address</div><div class="cell">City</div><div class="cell">State</div><div class="cell">Zip Code</div><div class="cell">Phone</div></div>
    <div class="row row--blank"><div class="cell"></div></div>
  </div>

  <div class="block" style="top:148px">
    <div class="block__head">Payment Information</div>
    <div class="row method" style="border-top:none"><div class="cell">Select Payment Method</div><div class="cell">Credit</div><div class="cell">Debit</div><div class="cell">Transfer</div></div>
  </div>

  <div class="block card-rows" style="top:188px">
    <div class="block__head">PAYMENT INFORMATION – Fill only If paid by credit card</div>
    <div class="row" style="border-top:none"><div class="cell">Name on Credit Card as it Appears</div><div class="cell"></div></div>
    <div class="row"><div class="cell">Credit Card Number</div><div class="cell"></div></div>
    <div class="row"><div class="cell">Expiration Date</div><div class="cell"></div></div>
    <div class="row"><div class="cell">Credit Card Billing Address</div><div class="cell"></div></div>
  </div>

  <div class="block" style="top:251px">
    <div class="block__head">PAYMENT INFORMATION – Fill only If paid by credit card</div>
    <div class="product"><div class="product__photo"><span role="img" aria-label="Photo of the vehicle tracking unit"></span></div><div class="product__body"><div class="product__details">Product Details:</div><div class="product__figures"><div>Price :</div><div>Quantity :</div><div>Total :</div></div></div></div>
    <div class="product"><div class="product__photo"><span role="img" aria-label="Photo of the wireless dash camera"></span></div><div class="product__body"><div class="product__details">Product Details:</div><div class="product__figures"><div>Price :</div><div>Quantity :</div><div>Total :</div></div></div></div>
    <div class="product"><div class="product__photo"><span role="img" aria-label="Photo of the tracker and dash camera bundle"></span></div><div class="product__body"><div class="product__details">Product Details:</div><div class="product__figures"><div>Price :</div><div>Quantity :</div><div>Total :</div></div></div></div>
  </div>

  <footer class="footer-band">www.northgatetracking.com</footer>
</section>

<section class="page page--plans">
  <header class="masthead">
    <svg class="masthead__panel" viewBox="0 0 339 53" preserveAspectRatio="none" aria-hidden="true"><polygon points="232,0 339,0 339,53 208,53" fill="#3589bb"/></svg>
    <div class="brand"><span class="brand__mark"></span><span class="brand__name">NORTHGATE</span></div>
    <address class="company"><strong>Northgate Tracking Ltd.</strong><br>418 Rue Marlowe, Quebec<br>H2X 4B7 Canada<br>1800 555 0142</address>
  </header>
  <h1 class="title-band">PAYMENT AUTHORIZATION</h1>

  <div class="block" style="top:85px">
    <div class="product"><div class="product__photo"><span role="img" aria-label="Photo of the vehicle tracking unit"></span></div><div class="product__body"><div class="product__details">Product Details:</div><div class="product__figures"><div>Price :</div><div>Quantity :</div><div>Total :</div></div></div></div>
    <div class="product"><div class="product__photo"><span role="img" aria-label="Photo of the wireless dash camera"></span></div><div class="product__body"><div class="product__details">Product Details:</div><div class="product__figures"><div>Price :</div><div>Quantity :</div><div>Total :</div></div></div></div>
    <div class="product"><div class="product__photo"><span role="img" aria-label="Photo of the tracker and dash camera bundle"></span></div><div class="product__body"><div class="product__details">Product Details:</div><div class="product__figures"><div>Price :</div><div>Quantity :</div><div>Total :</div></div></div></div>
    <div class="plans">
      <div class="plans__spacer"></div>
      <div class="plans__list">
        Monthly Plan: (Please check off)<br>
        <span class="box"></span>Base Plan, $24.99 per unit<br>
        <span class="box"></span>Pro Plan, $34.99 per unit<br>
        <span class="box box--checked"></span>ProPlus Plan, $39.99 per unit<br>
        <span class="box box--checked"></span>Camera Plan, $29.99 per unit
      </div>
    </div>
    <div class="sign">Signature</div>
    <div class="signoff"><div>Printed Name</div><div>Date</div></div>
    <div class="note">NOTE</div>
  </div>

  <footer class="footer-band">www.northgatetracking.com</footer>
</section>

<section class="page page--terms">
  <header class="masthead">
    <svg class="masthead__panel" viewBox="0 0 339 53" preserveAspectRatio="none" aria-hidden="true"><polygon points="232,0 339,0 339,53 208,53" fill="#3589bb"/></svg>
    <div class="brand"><span class="brand__mark"></span><span class="brand__name">NORTHGATE</span></div>
    <address class="company"><strong>Northgate Tracking Ltd.</strong><br>418 Rue Marlowe, Quebec<br>H2X 4B7 Canada<br>1800 555 0142</address>
  </header>
  <h1 class="title-band">TERMS AND CONDITIONS</h1>
  <footer class="footer-band">www.northgatetracking.com</footer>
</section>

</body>
</html>
```